Business card design needed

Double sided
Color, unique, elegant

Maybe put this quote somewhere?? But I think it might make it to cluttered?
“The Pilates Method of Body
Conditioning develops the body
uniformly, corrects posture, restores
vitality, invigorates the mind and
elevates the spirit”
- Henrik Dovacombe

Industry/Entity Type

Business

Contact Information for Business Card

Marta Kellbrook
Pilates Instructor & Personal trainer
Mobile: 0498265043
www.lorvix.com.au
email: lorvixhealth.fitness@qentamail.com

```html
<!DOCTYPE html>
<html lang="en">
<head>
<meta charset="utf-8">
<title>Lorvix Health and Fitness – Business Card</title>
<link href="https://fonts.googleapis.com/css2?family=Questrial&display=swap" rel="stylesheet">
<style>
  :root {
    --page-bg: #ecebea;
    --card-white: #ffffff;
    --blue-deep: #1468d8;
    --blue-mid: #22a4ea;
    --blue-light: #3ddcf8;
    --ice: #cdeefa;
    --text-blue: #1e8fe6;
    --name-green: #8cc25c;
    --name-pink: #cf6fb9;
    --wordmark-grey: #4a4a4a;
  }
  * { margin: 0; padding: 0; box-sizing: border-box; }
  html, body {
    width: 1200px;
    height: 1000px;
    overflow: hidden;
    background: var(--page-bg);
    font-family: "Questrial", "Century Gothic", sans-serif;
  }
  .canvas { position: relative; width: 1200px; height: 1000px; }

  .card {
    position: absolute;
    left: 258px;
    width: 686px;
    height: 381px;
    overflow: hidden;
    box-shadow: 0 3px 10px rgba(0,0,0,0.18);
  }

  /* Front */
  .card--front { top: 96px; }
  .front-backdrop {
    position: absolute; inset: 0;
    background: linear-gradient(35deg, var(--blue-deep) 0%, var(--blue-mid) 55%, var(--blue-light) 100%);
  }
  .front-lockup {
    position: absolute;
    left: 0; right: 0; top: 236px;
    text-align: center;
    color: #ffffff;
  }
  .front-lockup .wordmark {
    font-size: 58px;
    letter-spacing: 4px;
    line-height: 1;
  }
  .front-lockup .tagline {
    margin-top: 14px;
    font-size: 20px;
    letter-spacing: 0.3px;
  }

  /* Back */
  .card--back { top: 527px; background: var(--card-white); }
  .back-pattern {
    position: absolute;
    left: 0; top: 0;
    width: 345px; height: 381px;
    background:
      radial-gradient(ellipse at 55% 45%, rgba(173,224,246,0.55) 0%, rgba(205,238,250,0.35) 45%, rgba(255,255,255,0) 75%);
  }
  .back-lockup {
    position: absolute;
    left: 28px; top: 108px;
    width: 110px;
    text-align: center;
    color: var(--wordmark-grey);
  }
  .back-lockup .wordmark { font-size: 27px; letter-spacing: 1.5px; line-height: 1; }
  .back-lockup .tagline { margin-top: 5px; font-size: 10px; }

  .contact-person {
    position: absolute;
    right: 26px; top: 165px;
    text-align: right;
  }
  .contact-person .name { font-size: 29px; line-height: 1.1; }
  .name .given { color: var(--name-green); }
  .name .family { color: var(--name-pink); }
  .contact-person .role {
    margin-top: 6px;
    font-size: 16px;
    color: var(--text-blue);
  }

  .contact-list {
    position: absolute;
    left: 318px; top: 280px;
    color: var(--text-blue);
    font-size: 16.5px;
  }
  .contact-row { display: flex; height: 29px; align-items: center; }
  .contact-row dt { width: 64px; text-align: right; margin-right: 16px; }
  .contact-row dd { white-space: nowrap; }
</style>
</head>
<body>
<div class="canvas">

  <section class="card card--front" aria-label="Business card front">
    <div class="front-backdrop" role="img" aria-label="Blue mosaic of soft square tiles shading from deep blue to cyan"></div>
    <div class="front-lockup">
      <div class="wordmark">LORVIX</div>
      <div class="tagline">Health and Fitness</div>
    </div>
  </section>

  <section class="card card--back" aria-label="Business card back">
    <div class="back-pattern" role="img" aria-label="Faint pale blue mosaic of square tiles"></div>
    <div class="back-lockup">
      <div class="wordmark">LORVIX</div>
      <div class="tagline">Health and Fitness</div>
    </div>

    <div class="contact-person">
      <div class="name"><span class="given">Marta</span> <span class="family">Kellbrook</span></div>
      <div class="role">Pilates Instructor &amp; Personal trainer</div>
    </div>

    <dl class="contact-list">
      <div class="contact-row"><dt>Phone:</dt><dd>0498 265 043</dd></div>
      <div class="contact-row"><dt>E-mail:</dt><dd>lorvixhealth.fitness@qentamail.com</dd></div>
      <div class="contact-row"><dt>Web:</dt><dd>www.lorvix.com.au</dd></div>
    </dl>
  </section>

</div>
</body>
</html>
```